"Maple Hollow" red wine label design

We are a Sydney based company. We need to design a wine label for a Australian red wine.
Front label include following info:
Our brand: "Maple Hollow";
Product name: "Shiraz 2016";
In the bottom with small font: "Wine of Australia", "750ml"
Back label:
the back label would need to be consistent with the front label, with space for one paragraph of tasting notes, and ingredient info etc.
we would like to use white, gold and blue in this label. It should make customer feel the magical and beautiful moment of starry night.

We also need a logo design for the wine brand: "Maple Hollow"

I have attached a few wine bottle that used blue to give you some inspirations.

We need the design in AI file format.

Target Market(s)

both men and women

Industry/Entity Type

It Company

Logo Text

Maple Hollow

Requirements
Nice to have
• gold borderline, words; use of blue and white

```html
<!DOCTYPE html>
<html lang="en">
<head>
<meta charset="utf-8">
<title>Maple Hollow – Shiraz 2016 Label</title>
<link rel="stylesheet" href="https://fonts.googleapis.com/css2?family=Great+Vibes&family=Cormorant+Garamond:wght@500&family=Arimo&display=swap">
<style>
  :root {
    --page-bg: #ffffff;
    --sky-deep: #191a33;
    --sky-mid: #2b2f66;
    --sky-violet: #3e2f70;
    --sky-haze: #4a5391;
    --gold: #d8bd79;
    --ink-white: #ffffff;
  }
  * { margin: 0; padding: 0; box-sizing: border-box; }
  html, body { width: 676px; height: 1200px; overflow: hidden; background: var(--page-bg); }
  .canvas { position: relative; width: 676px; height: 1200px; }
  .label {
    position: absolute; left: 2px; top: 184px; width: 672px; height: 843px;
    border-radius: 12px; overflow: hidden; color: var(--ink-white); text-align: center;
  }
  .label__sky {
    position: absolute; inset: 0;
    background:
      radial-gradient(ellipse 340px 260px at 560px 240px, rgba(110,60,160,0.45), transparent 70%),
      radial-gradient(ellipse 300px 420px at 300px 300px, rgba(90,105,170,0.35), transparent 70%),
      radial-gradient(ellipse 260px 200px at 60px 380px, rgba(90,40,130,0.35), transparent 70%),
      linear-gradient(180deg, var(--sky-mid) 0%, var(--sky-violet) 35%, var(--sky-mid) 62%, var(--sky-deep) 85%, var(--sky-deep) 100%);
  }
  .label__winery {
    position: absolute; top: 68px; left: 0; right: 0;
    font: 500 25px/1 "Cormorant Garamond", serif; font-variant: small-caps; letter-spacing: 0.5px;
  }
  .label__brand {
    position: absolute; top: 262px; left: 0; right: 0;
    font: 400 104px/112px "Great Vibes", cursive;
  }
  .label__flourish {
    position: absolute; top: 527px; left: 305px; width: 62px; height: 38px;
    background: var(--gold); opacity: 0.85; border-radius: 19px;
  }
  .label__variety {
    position: absolute; top: 598px; left: 0; right: 0;
    font: 500 34px/40px "Cormorant Garamond", serif; font-variant: small-caps; letter-spacing: 1px;
  }
  .label__vintage { display: block; font-variant: normal; letter-spacing: 0; }
  .label__details {
    position: absolute; top: 760px; left: 0; right: 0;
    font: 400 15.5px/26px "Arimo", sans-serif;
  }
</style>
</head>
<body>
<div class="canvas">
  <section class="label">
    <div class="label__sky" role="img" aria-label="Night sky with the Milky Way and scattered gold stars"></div>
    <p class="label__winery">Winery logo</p>
    <h1 class="label__brand">Maple<br>Hollow</h1>
    <div class="label__flourish" role="img" aria-label="Small gold decorative flourish"></div>
    <p class="label__variety">Shiraz<span class="label__vintage">2016</span></p>
    <p class="label__details">Wine of Australia<br>750ml&nbsp;&nbsp;13,5% Alc.Vol.</p>
  </section>
</div>
</body>
</html>
```